A Label for an ECO Friendly Spirit Company

Design a label which can be used for vodka and gin (London Dry Gin). It should be Square type Like the Shape File you see in the uploads. VORK means Local Eco friendly Authentic and Fair. We want a cool and slim label that calls for eco-friendly. We want to use it for our premium
Vodka and our London Dry Gin. Please use the logo and design it in Square Type.

40%vol, 700ml

Target Market(s)

spirits and events

Industry/Entity Type

SPIRITS

Colors
00AB8E
00BBA5
67D7C9
C6EFE9
E9F9F6
59FF00
82FF00
B8FF75
E3FFCB
F4FFEA

Requirements
Must have
• Logo from VORK, Squaee Shape

```html
<!DOCTYPE html>
<html lang="en">
<head>
<meta charset="utf-8">
<title>VORK Spirit Labels</title>
<link href="https://fonts.googleapis.com/css2?family=Rye&family=Montserrat:wght@600&family=Oswald:wght@500&family=Share+Tech+Mono&display=swap" rel="stylesheet">
<style>
  :root {
    --teal: #0fa98b;
    --green: #8cc63f;
    --cream: #fdebd4;
    --watermark: #ebe5bd;
    --page: #ffffff;
  }
  html, body {
    margin: 0;
    padding: 0;
    width: 1200px;
    height: 1000px;
    overflow: hidden;
    background: var(--page);
  }
  .canvas {
    position: relative;
    width: 1200px;
    height: 1000px;
  }
  .label {
    position: absolute;
    top: 237px;
    width: 505px;
    height: 505px;
  }
  .label--vodka { left: 66px; }
  .label--gin { left: 619px; }
  .label__shape {
    position: absolute;
    inset: 0;
  }
  .label__text {
    position: absolute;
    left: 50%;
    transform: translateX(-50%);
    margin: 0;
    white-space: nowrap;
    text-align: center;
  }
  .brand-mark {
    position: absolute;
    left: 50%;
    top: 98px;
    width: 40px;
    height: 32px;
    margin-left: -20px;
    border-radius: 5px;
    background: var(--green);
  }
  .brand-name {
    top: 116px;
    font-family: "Montserrat", sans-serif;
    font-weight: 600;
    font-size: 29px;
    letter-spacing: 1px;
    color: var(--teal);
  }
  .product-name {
    font-family: "Rye", serif;
    font-weight: 400;
    line-height: 1;
  }
  .label--vodka .product-name {
    top: 232px;
    font-size: 74px;
    color: var(--green);
  }
  .label--gin .product-name {
    top: 176px;
    font-size: 62px;
    line-height: 92px;
    color: var(--teal);
  }
  .tagline {
    font-family: "Oswald", sans-serif;
    font-weight: 500;
    font-size: 15px;
    letter-spacing: 0.5px;
  }
  .tagline--local { top: 352px; color: var(--green); }
  .tagline--premium { top: 375px; }
  .label--vodka .tagline--premium { color: var(--green); }
  .label--gin .tagline--premium { color: var(--teal); }
  .spec {
    font-family: "Share Tech Mono", monospace;
    font-size: 11px;
    line-height: 14px;
    color: var(--green);
    top: 408px;
  }
</style>
</head>
<body>
<main class="canvas">

  <section class="label label--vodka" aria-label="Vodka label">
    <svg class="label__shape" viewBox="0 0 505 505" width="505" height="505" aria-hidden="true">
      <polygon points="252.5,0 505,252.5 252.5,505 0,252.5" fill="var(--teal)"/>
      <polygon points="252.5,18 487,252.5 252.5,487 18,252.5" fill="var(--cream)"/>
      <rect x="135" y="125" width="240" height="250" rx="18" fill="var(--watermark)" opacity="0.75"/>
    </svg>
    <span class="brand-mark" aria-hidden="true"></span>
    <p class="label__text brand-name">VORK</p>
    <h2 class="label__text product-name">VODKA</h2>
    <p class="label__text tagline tagline--local">LOCAL AUTHENTIC</p>
    <p class="label__text tagline tagline--premium">PREMIUM</p>
    <p class="label__text spec">40%<br>VOL. 700ML</p>
  </section>

  <section class="label label--gin" aria-label="London Dry Gin label">
    <svg class="label__shape" viewBox="0 0 505 505" width="505" height="505" aria-hidden="true">
      <polygon points="252.5,0 505,252.5 252.5,505 0,252.5" fill="var(--green)"/>
      <polygon points="252.5,18 487,252.5 252.5,487 18,252.5" fill="var(--cream)"/>
      <rect x="135" y="125" width="240" height="250" rx="18" fill="var(--watermark)" opacity="0.75"/>
    </svg>
    <span class="brand-mark" aria-hidden="true"></span>
    <p class="label__text brand-name">VORK</p>
    <h2 class="label__text product-name">LONDON<br>DRY GIN</h2>
    <p class="label__text tagline tagline--local">LOCAL AUTHENTIC</p>
    <p class="label__text tagline tagline--premium">PREMIUM</p>
    <p class="label__text spec">40%<br>VOL. 700ML</p>
  </section>

</main>
</body>
</html>
```